Marlow Crest Group (Real Estate and Investment)

A high end, clean design.
We are a real estate company with sales, asset management and investment divisions. We want to use a black and white scheme which is really high end feel. The back of the card can just be the logo (black background with the white writing) as we will probably emboss this when we print)

Target Market(s)

High level investors, high end houses for sale

Industry/Entity Type

Business

Contact Information for Business Card

Name, position, phone number and email address
Glen Varley, Managing Director, 0437259064 and glen@marlowcrest-example.com.au

Requirements
Must have
• Back of the card to be the black background with the white writing (as per the attached images). Would like the capacity to emboss the writing and logo

```html
<!DOCTYPE html>
<html lang="en">
<head>
<meta charset="UTF-8">
<title>Marlow Crest Group – Business Card</title>
<link rel="stylesheet" href="https://fonts.googleapis.com/css2?family=Montserrat:wght@400;500;700&display=swap">
<style>
  :root {
    --canvas: #e4e4e4;
    --card-black: #000000;
    --card-dark: #1b1c1d;
    --accent: #f6a90f;
    --stripe-grey: #1a1a1a;
    --text-light: #ffffff;
    --photo-sky: #c9cdd2;
    --photo-wall: #a59d93;
    --photo-lawn: #4d7a33;
    --night-top: #232527;
    --night-bottom: #141614;
  }
  * { margin: 0; padding: 0; box-sizing: border-box; }
  html, body {
    width: 1200px; height: 1200px; overflow: hidden;
    background: var(--canvas);
    font-family: "Montserrat", Arial, sans-serif;
  }
  .canvas { position: relative; width: 1200px; height: 1200px; }

  .card {
    position: absolute;
    width: 902px; height: 542px;
    transform: scale(0.8);
    transform-origin: top left;
    overflow: hidden;
    box-shadow: 0 20px 40px rgba(0,0,0,0.25);
  }
  .card--front { left: 238px; top: 106px; background: var(--card-black); }
  .card--back  { left: 240px; top: 630px; background: var(--card-dark); }

  .card__art { position: absolute; inset: 0; width: 902px; height: 542px; }

  .brand {
    position: absolute;
    display: flex; flex-direction: column; align-items: center;
    color: var(--text-light);
  }
  .brand__mark {
    width: 86px; height: 86px; border-radius: 50%;
    border: 1.5px solid var(--text-light);
  }
  .brand__name {
    margin-top: 16px;
    font-weight: 400; font-size: 22px; letter-spacing: 0.5px;
    white-space: nowrap;
  }
  .card--front .brand { left: 40px; top: 48px; width: 220px; }
  .card--back .brand { left: 0; right: 0; top: 142px; }
  .card--back .brand__mark { width: 124px; height: 124px; }
  .card--back .brand__name { font-size: 30px; margin-top: 22px; }

  .person { position: absolute; left: 44px; top: 262px; color: var(--text-light); }
  .person__name { font-size: 42px; font-weight: 400; line-height: 1.1; }
  .person__name strong { font-weight: 700; }
  .person__role { font-size: 15px; font-weight: 500; letter-spacing: 0.6px; margin-top: 2px; }

  .contact { position: absolute; left: 44px; top: 366px; color: var(--text-light); list-style: none; }
  .contact__item { display: flex; align-items: center; height: 34px; font-size: 19px; letter-spacing: 0.6px; }
  .contact__icon { width: 24px; height: 24px; margin-right: 22px; fill: var(--accent); }

  .back__band {
    position: absolute; left: 0; bottom: 0; width: 100%; height: 30px;
    background: var(--accent);
  }
</style>
</head>
<body>
<main class="canvas">

  <section class="card card--front" aria-label="Business card front">
    <svg class="card__art" viewBox="0 0 902 542" aria-hidden="false">
      <defs>
        <linearGradient id="houseDay" x1="0" y1="0" x2="0" y2="1">
          <stop offset="0" stop-color="var(--photo-sky)"/>
          <stop offset="0.65" stop-color="var(--photo-wall)"/>
          <stop offset="1" stop-color="var(--photo-lawn)"/>
        </linearGradient>
      </defs>
      <polygon role="img" aria-label="Photograph of a modern two-storey luxury home"
               points="470,82 878,0 902,0 902,542 870,542" fill="url(#houseDay)"/>
      <polyline points="462,80 874,0" fill="none" stroke="var(--accent)" stroke-width="4"/>
      <polyline points="462,80 900,540" fill="none" stroke="var(--accent)" stroke-width="4"/>
      <polygon points="530,213 820,542 740,542" fill="var(--accent)"/>
      <polygon points="572,340 702,542 670,542" fill="var(--stripe-grey)"/>
    </svg>

    <div class="brand">
      <span class="brand__mark"></span>
      <span class="brand__name">MARLOW CREST GROUP</span>
    </div>

    <div class="person">
      <h1 class="person__name">Glen <strong>Varley</strong></h1>
      <p class="person__role">Managing Director</p>
    </div>

    <ul class="contact">
      <li class="contact__item">
        <svg class="contact__icon" viewBox="0 0 24 24"><path d="M6.6 10.8a15.1 15.1 0 0 0 6.6 6.6l2.2-2.2a1 1 0 0 1 1-.25 11.4 11.4 0 0 0 3.6.57 1 1 0 0 1 1 1V20a1 1 0 0 1-1 1A17 17 0 0 1 3 4a1 1 0 0 1 1-1h3.5a1 1 0 0 1 1 1c0 1.25.2 2.45.57 3.57a1 1 0 0 1-.25 1z"/></svg>
        0437259064
      </li>
      <li class="contact__item">
        <svg class="contact__icon" viewBox="0 0 24 24"><path d="M12 2 2 9v12h20V9zm0 2.4 7.6 5.2L12 14 4.4 9.6zM4 19v-7.2l8 4.6 8-4.6V19z"/></svg>
        glen@marlowcrest-example.com.au
      </li>
    </ul>
  </section>

  <section class="card card--back" aria-label="Business card back">
    <svg class="card__art" viewBox="0 0 902 542">
      <defs>
        <linearGradient id="houseNight" x1="0" y1="0" x2="0" y2="1">
          <stop offset="0" stop-color="var(--night-top)"/>
          <stop offset="0.75" stop-color="#262624"/>
          <stop offset="1" stop-color="var(--night-bottom)"/>
        </linearGradient>
      </defs>
      <rect role="img" aria-label="Darkened photograph of a modern luxury home at dusk"
            x="0" y="0" width="902" height="542" fill="url(#houseNight)"/>
    </svg>
    <div class="brand">
      <span class="brand__mark"></span>
      <span class="brand__name">MARLOW CREST GROUP</span>
    </div>
    <div class="back__band"></div>
  </section>

</main>
</body>
</html>
```